Business Card for my Photography/Video Business

I would like the card to say Event Photographer and Videographer. I like the Black and Gold look to it as well but open to other options. I don't want it to be super vibrant or colorful. Simple, elegant and professional

```html
<!DOCTYPE html>
<html lang="en">
<head>
<meta charset="utf-8">
<title>Lumen Frame – Business Card</title>
<link href="https://fonts.googleapis.com/css2?family=Great+Vibes&family=Montserrat:wght@600&family=Open+Sans:wght@400;600&display=swap" rel="stylesheet">
<style>
  :root {
    --backdrop: #d9d9db;
    --card: #0b0b0b;
    --card-edge: #1a1a1a;
    --gold: #d1ad4c;
    --gold-light: #f2dc8c;
    --gold-deep: #a97f26;
    --contact-text: #c8b27a;
    --ink: #111111;
  }
  * { margin: 0; padding: 0; box-sizing: border-box; }
  html, body {
    width: 1200px; height: 1200px; overflow: hidden;
    background: var(--backdrop);
  }
  .sheet {
    position: relative; width: 1200px; height: 1200px;
    display: flex; flex-direction: column; align-items: center; justify-content: center;
    gap: 60px;
  }
  .card {
    position: relative; width: 840px; height: 480px;
    background: radial-gradient(circle at 50% 40%, var(--card-edge) 0%, var(--card) 60%);
    border-radius: 4px;
    box-shadow: 0 18px 40px rgba(0,0,0,0.28);
    overflow: hidden;
  }

  /* Front */
  .brand {
    position: absolute; inset: 0;
    display: flex; flex-direction: column; align-items: center; justify-content: center; gap: 22px;
  }
  .brand-dot {
    width: 130px; height: 130px; border-radius: 50%;
    background: var(--gold);
  }
  .brand-name {
    font-family: "Montserrat", sans-serif; font-weight: 600;
    font-size: 64px; line-height: 1; letter-spacing: 4px; text-transform: uppercase;
    color: var(--gold);
  }

  /* Back */
  .back-art { position: absolute; inset: 0; }
  .person {
    position: absolute; left: 150px; top: 34px;
    font-family: "Great Vibes", cursive; font-weight: 400; font-size: 84px; line-height: 1;
    color: var(--gold);
  }
  .role {
    position: absolute; left: 150px; top: 124px; width: 560px;
    font-family: "Open Sans", sans-serif; font-weight: 600;
    font-size: 13px; letter-spacing: 4px; color: var(--gold-light);
    white-space: nowrap;
  }
  .contacts {
    position: absolute; left: 130px; top: 170px;
    list-style: none;
    font-family: "Open Sans", sans-serif; font-size: 20px; color: var(--contact-text);
  }
  .contacts li { display: flex; align-items: center; gap: 12px; height: 34px; }
  .contacts svg { width: 18px; height: 18px; fill: #e9e9e9; flex: none; }
  .address {
    position: absolute; left: 58px; top: 305px;
    display: flex; align-items: center; gap: 10px;
    font-family: "Open Sans", sans-serif; font-size: 20px; color: var(--ink);
  }
  .address svg { width: 18px; height: 18px; fill: var(--ink); }
</style>
</head>
<body>
<main class="sheet">

  <section class="card card-front" aria-label="Card front">
    <div class="brand">
      <span class="brand-dot"></span>
      <span class="brand-name">Lumen Frame</span>
    </div>
  </section>

  <section class="card card-back" aria-label="Card back">
    <svg class="back-art" viewBox="0 0 840 480" aria-hidden="true">
      <defs>
        <linearGradient id="goldBand" x1="0" y1="0" x2="1" y2="1">
          <stop offset="0" stop-color="#b8902e"/>
          <stop offset="0.45" stop-color="#f2dc8c"/>
          <stop offset="0.75" stop-color="#d1ad4c"/>
          <stop offset="1" stop-color="#a97f26"/>
        </linearGradient>
      </defs>
      <line class="band-rule" x1="0" y1="292" x2="840" y2="292" stroke="#8c7640" stroke-width="1"/>
      <line class="band-rule" x1="0" y1="356" x2="840" y2="356" stroke="#8c7640" stroke-width="1"/>
      <rect class="gold-band" x="0" y="298" width="660" height="52" fill="url(#goldBand)"/>
      <circle class="seal-ring" cx="680" cy="324" r="64" fill="var(--card)"/>
      <circle class="seal" cx="680" cy="324" r="56" fill="url(#goldBand)"/>
    </svg>

    <h1 class="person">Rowan Hale</h1>
    <p class="role">EVENT PHOTOGRAPHER AND VIDEOGRAPHER</p>

    <ul class="contacts">
      <li>
        <svg viewBox="0 0 24 24"><path d="M6.6 10.8a15 15 0 0 0 6.6 6.6l2.2-2.2a1 1 0 0 1 1-.25 11.4 11.4 0 0 0 3.6.57 1 1 0 0 1 1 1V20a1 1 0 0 1-1 1A17 17 0 0 1 3 4a1 1 0 0 1 1-1h3.5a1 1 0 0 1 1 1c0 1.25.2 2.450.57 3.57a1 1 0 0 1-.25 1z"/></svg>
        1-555-01427
      </li>
      <li>
        <svg viewBox="0 0 24 24"><path d="M12 2a10 10 0 1 0 0 20 10 10 0 0 0 0-20zm6.9 6h-2.9a15.6 15.6 0 0 0-1.4-3.6A8 8 0 0 1 18.9 8zM12 4c.8 1.2 1.5 2.5 1.9 4h-3.8c.4-1.5 1.1-2.8 1.9-4zM4.3 14a8 8 0 0 1 0-4h3.4a16 16 0 0 0 0 4zm.8 2h2.9c.3 1.3.8 2.5 1.4 3.6A8 8 0 0 1 5.1 16zM8 8H5.1a8 8 0 0 1 4.3-3.6C8.8 5.5 8.4 6.7 8 8zm4 12c-.8-1.2-1.5-2.5-1.9-4h3.8c-.4 1.5-1.1 2.8-1.900 4zm2.3-6H9.7a14.7 14.7 0 0 1 0-4h4.6a14.7 14.7 0 0 1 0 4zm.3 5.6c.6-1.1 1.1-2.3 1.4-3.6h2.9a8 8 0 0 1-4.3 3.6zm1.7-5.6a16 16 0 0 0 0-4h3.4a8 8 0 0 1 0 4z"/></svg>
        www.lumenframe.com
      </li>
      <li>
        <svg viewBox="0 0 24 24"><path d="M2 5h20v14H2zm2 2v.5l8 5 8-5V7zm16 2.8-8 5-8-5V17h16z"/></svg>
        rowan@lumenframe.com
      </li>
    </ul>

    <p class="address">
      <svg viewBox="0 0 24 24"><path d="M12 2a7 7 0 0 0-7 7c0 5.2 7 13 7 13s7-7.8 7-13a7 7 0 0 0-7-7zm0 9.5A2.5 2.5 0 1 1 12 6.5a2.5 2.5 0 0 1 0 5z"/></svg>
      Harbor City, Westland Coast
    </p>
  </section>

</main>
</body>
</html>
```